Town Planning Consultants require lstationary design

Require a design to be used for our letterhead and report cover page. We have an approved logo.
we have attached our logo, and our temporary letterhead/cover page (SEE Cover) which we currently adapt for both purposes in the interim pending a permanent design. I have also attached an example (example report cover) of a report cover page that I like. perhaps similar with our colour scheme

Target Market(s)

?

Industry/Entity Type

Town

Colors
249fd4
3176b5

Requirements
Must have
• colours to match logo
• the text content in existing letterhead

```html
<!DOCTYPE html>
<html lang="en">
<head>
<meta charset="utf-8">
<title>Brightfield Letterhead</title>
<link href="https://fonts.googleapis.com/css2?family=Lato:wght@400;700&display=swap" rel="stylesheet">
<style>
  :root {
    --brand-blue: #2ea8dc;
    --brand-deep: #3176b5;
    --paper: #e8e8e8;
    --ink: #3d3d3d;
    --ink-soft: #555555;
    --mark-grey: #9a9a9a;
    --band-grey: #9c9c9c;
    --white: #ffffff;
  }
  * { box-sizing: border-box; margin: 0; padding: 0; }
  html, body { width: 900px; height: 1200px; overflow: hidden; background: var(--paper); }
  body { font-family: "Lato", Arial, sans-serif; color: var(--ink); }
  .letterhead { position: relative; width: 900px; height: 1200px; background: var(--paper); overflow: hidden; }

  .top-band { position: absolute; left: 0; top: 0; width: 900px; height: 96px; background: var(--brand-blue); }
  .services { position: absolute; right: 42px; top: 36px; color: var(--white); font-size: 21px; letter-spacing: 0.2px; }

  .brand { position: absolute; left: 54px; top: 40px; display: flex; align-items: flex-end; gap: 14px; }
  .brand-square { width: 58px; height: 58px; background: var(--brand-blue); border: 3px solid var(--white); }
  .brand-name { font-size: 62px; font-weight: 400; color: var(--mark-grey); line-height: 1; margin-bottom: -20px; }

  .letter { position: absolute; left: 65px; top: 375px; width: 790px; font-size: 14.5px; line-height: 18.6px; color: var(--ink); }
  .salutation { font-weight: 700; margin-bottom: 36px; }
  .letter p { margin-bottom: 18.6px; text-align: justify; }

  .sign-off { position: absolute; left: 65px; top: 786px; font-size: 14.5px; line-height: 20px; color: var(--ink); }
  .signer-name { font-weight: 700; }
  .signature { position: absolute; left: 205px; top: 822px; width: 135px; height: 40px; background: linear-gradient(90deg, rgba(49,118,181,0.18), rgba(49,118,181,0.05)); border-radius: 20px; }

  .footer-band { position: absolute; left: 0; top: 1115px; width: 900px; height: 48px; background: var(--brand-blue); color: var(--white); font-size: 15px; line-height: 20px; }
  .footer-grey { position: absolute; right: 0; top: 0; width: 94px; height: 48px; background: var(--band-grey); }
  .footer-address { position: absolute; left: 58px; top: 4px; }
  .footer-phones { position: absolute; left: 316px; top: 4px; }
  .footer-email { position: absolute; left: 541px; top: 14px; }
  .label { font-weight: 700; }
</style>
</head>
<body>
  <div class="letterhead">
    <header class="top-band">
      <div class="services">Planning | Development | Urban Design</div>
    </header>
    <div class="brand">
      <div class="brand-square"></div>
      <div class="brand-name">Brightfield</div>
    </div>

    <main class="letter">
      <div class="salutation">Dear Mr. Carter,</div>
      <p>Lorem ipsum dolor sit amet, consectetur adipiscing elit. Donec orci purus, luctus vitae dignissim eu, iaculis sed purus. Vivamus faucibus, ipsum nec aliquet viverra, leo mauris condimentum ligula, sit amet sagittis enim ligula quis arcu. Nam egestas tortor id nisi porttitor mattis. In tortor ante, ultricies in suscipit a, tempus non massa. Vivamus et auctor mi.</p>
      <p>Fusce vel massa nulla. Phasellus nec eros mauris, et scelerisque orci. Donec malesuada orci vitae nulla accumsan porta a id massa. Quisque accumsan iaculis magna sit amet fringilla. Maecenas consequat, magna eget tincidunt semper, odio nibh rutrum mi, id feugiat ante nisi eu risus. Vestibulum nunc orci, rhoncus a placerat in, ultricies in mi. Cras mattis varius eros, vel fringilla nisi suscipit eget.</p>
      <p>Quisque scelerisque sagittis nulla at porttitor. Mauris a justo et tellus interdum tristique. Sed id augue vitae urna euismod commodo aliquet a quam. Pellentesque arcu velit, cursus et malesuada ut, consequat et diam. Nullam erat sem, rhoncus id ullamcorper vitae, rhoncus et arcu. In ultricies ultricies nulla, ut rutrum nisi iaculis at. Donec eu magna a metus ornare faucibus.</p>
      <p>Fusce aliquet faucibus ultricies. Morbi semper, est id tincidunt gravida, sem arcu adipiscing lacus, ac bibendum nulla leo eu purus. Quisque nec diam sed risus consectetur a ccumsan quis quis nibh. Vestibulum id purus lorem.</p>
    </main>

    <div class="sign-off">
      <div class="signer-name">Alex Morgan</div>
      <div class="signer-role">Co-Founder &amp; CEO</div>
    </div>
    <div class="signature" role="img" aria-label="Handwritten signature of Alex Morgan"></div>

    <footer class="footer-band">
      <div class="footer-address">12 Harbour View Road<br>KELLSBURY NSW 2400</div>
      <div class="footer-phones"><span class="label">P :</span> +61 (2) 5550 1234<br><span class="label">M :</span> +61 (0)400 555 012</div>
      <div class="footer-email"><span class="label">E :</span> alex@brightfield.com.au</div>
      <div class="footer-grey"></div>
    </footer>
  </div>
</body>
</html>
```